quarry-mosaic artisans and studio

I need a web design for my company we offer counter tops. tile for floors,showers,kitchen backsplashes and more also need a place where the client
can write reviews

```html
<!DOCTYPE html>
<html lang="en">
<head>
<meta charset="utf-8">
<title>Quarry-Mosaic Artisans</title>
<link rel="stylesheet" href="https://fonts.googleapis.com/css2?family=Arimo:ital,wght@0,400;0,700;1,400&family=Noto+Serif:ital@1&display=swap">
<style>
:root{
  --accent:#f15a24;
  --ink:#333333;
  --text:#555555;
  --muted:#999999;
  --line:#e3e3e3;
  --panel:#f7f7f7;
  --dark:#353535;
  --white:#ffffff;
}
*{margin:0;padding:0;box-sizing:border-box}
html,body{width:1200px;height:1046px;overflow:hidden;background:var(--white)}
body{position:relative;font-family:"Arimo",Arial,sans-serif;color:var(--text)}
.abs{position:absolute}
.top-rule{left:0;top:0;width:1200px;height:4px;background:var(--dark)}
.tool-toggle{left:0;top:45px;width:35px;height:35px;background:#e9e9e9;border:1px solid #d6d6d6}
.brand-group{left:183px;top:28px;display:flex;align-items:baseline;gap:12px;white-space:nowrap}
.brand{font-size:28px;color:var(--ink);letter-spacing:-0.3px}
.slogan{font-size:11px;color:var(--muted)}
.contact-group{right:287px;top:42px;display:flex;align-items:center;gap:18px;white-space:nowrap}
.contact{font-size:11px;display:flex;align-items:center;gap:6px}
.contact.email{color:var(--accent)}
.contact.phone{color:var(--ink)}
.social{left:936px;top:37px;display:flex;gap:6px}
.social span{width:22px;height:22px;border-radius:50%;background:#9a9a9a}
.nav{left:183px;top:87px;width:839px;height:37px;border:1px solid var(--line);background:linear-gradient(#fff,#f5f5f5);display:flex}
.nav a{width:93px;height:35px;line-height:35px;text-align:center;font-size:11px;font-weight:700;color:var(--ink);text-decoration:none;border-right:1px solid var(--line)}
.nav a.active{background:var(--accent);color:var(--white)}
.hero{left:183px;top:137px;width:839px;height:313px;background:linear-gradient(160deg,#3a3530 0%,#8a6a4a 35%,#c79a62 55%,#b07848 75%,#d9d2c6 100%)}
.caption{left:183px;top:316px;width:312px;height:95px;background:rgba(25,25,25,.8);padding:18px 17px}
.caption h2{font-size:18px;color:var(--white);font-weight:700;margin-bottom:8px}
.caption p{font-size:10.5px;line-height:16px;color:#e6e6e6}
.caption p a{color:var(--accent);text-decoration:none}
.dots{left:183px;top:412px;width:87px;height:25px;background:rgba(25,25,25,.85);display:flex;align-items:center;gap:7px;padding-left:13px}
.dots span{width:6px;height:6px;background:var(--white)}
.dots span.on{background:var(--accent)}
.hero-arrows{left:973px;top:412px;display:flex;gap:1px}
.hero-arrows span{width:24px;height:24px;background:var(--accent);display:flex;align-items:center;justify-content:center}
.callout{left:183px;top:463px;width:839px;height:87px;background:var(--panel);border:1px solid var(--line);border-left:3px solid var(--accent);padding:17px 0 0 19px}
.callout h3{font-size:16px;color:var(--ink);font-weight:700;margin-bottom:6px}
.callout p{font-size:11px;line-height:16px;width:665px}
.btn{background:var(--accent);color:var(--white);font-size:15px;display:flex;align-items:center;justify-content:center}
.callout .btn{position:absolute;left:700px;top:14px;width:118px;height:37px}
.section-title{font-size:16px;font-weight:700;color:var(--ink)}
.section-title em{font-size:11px;font-weight:400;color:var(--accent)}
.section-rule{height:1px;background:var(--line)}
.mini-arrows{display:flex;gap:1px}
.mini-arrows span{width:17px;height:17px;background:#dedede;display:flex;align-items:center;justify-content:center}
.project{top:631px;width:197px}
.project .thumb{height:117px;background:linear-gradient(150deg,#e8e4dc 0%,#b9c6a0 35%,#9b6a3e 70%,#d8cfc2 100%)}
.project .thumb.dark{background:linear-gradient(150deg,#f0ede8 0%,#5a3524 45%,#2a2420 75%,#e4ddd4 100%)}
.project h4{text-align:center;font-size:12px;font-weight:700;color:var(--ink);margin-top:11px;letter-spacing:.3px}
.project .nudge{position:absolute;top:47px;width:20px;height:22px;background:var(--accent);display:flex;align-items:center;justify-content:center}
.news-copy{left:183px;top:868px;width:410px;font-size:11px;line-height:16px;color:var(--ink)}
.field{left:183px;top:917px;width:323px;height:26px;border:1px solid var(--line);font-size:11px;color:var(--muted);padding:7px 10px}
.subscribe{left:516px;top:917px;width:77px;height:26px;font-size:11px}
.note{left:183px;top:957px;font-size:9px;font-style:italic;color:var(--muted)}
.note b{color:var(--accent);font-weight:400}
.quote{left:610px;top:868px;width:410px;height:84px;border:1px solid var(--line);background:#fafafa;padding:14px 12px 0 36px;font-family:"Noto Serif",Georgia,serif;font-style:italic;font-size:12px;line-height:19px;color:#888}
.quote .mark{position:absolute;left:13px;top:10px;font-size:26px;color:#ccc}
.quote-tail{left:930px;top:951px}
.author{left:610px;width:356px;text-align:right;font-size:11px}
.footer{left:0;top:1011px;width:1200px;height:35px;background:var(--dark);font-size:10px;color:#bbb}
.footer .copy{position:absolute;left:180px;top:14px}
.footer .links{position:absolute;right:183px;top:14px;color:var(--white)}
.footer .links i{font-style:normal;color:#888;margin:0 3px}
.to-top{left:1157px;top:1011px;width:26px;height:22px;background:#888;display:flex;align-items:center;justify-content:center}
</style>
</head>
<body>
<div class="abs top-rule"></div>
<div class="abs tool-toggle">
  <svg width="35" height="35" viewBox="0 0 35 35"><g stroke="#333" stroke-width="2.4" stroke-linecap="round"><line x1="9" y1="26" x2="24" y2="11"/><line x1="10" y1="10" x2="25" y2="25"/></g><circle cx="25" cy="10" r="3.5" fill="none" stroke="#333" stroke-width="2"/></svg>
</div>

<header class="abs brand-group">
  <span class="brand">Quarry-Mosaic Artisans</span>
  <span class="slogan">Your Slogan here</span>
</header>
<div class="abs contact-group">
  <div class="contact email"><svg width="13" height="9" viewBox="0 0 13 9"><rect x=".5" y=".5" width="12" height="8" fill="none" stroke="#aaa"/><path d="M.5 .5 6.5 5 12.5 .5" fill="none" stroke="#aaa"/></svg>hello@qmosaic.example</div>
  <div class="contact phone"><svg width="13" height="13" viewBox="0 0 13 13"><path d="M2 1 5 1 6 4 4 5.5Q5.5 8 7.5 9L9 7 12 8 12 11Q6 12 2 7 0 3 2 1Z" fill="#aaa"/></svg>(555) 014-2283</div>
</div>
<div class="abs social"><span></span><span></span><span></span></div>

<nav class="abs nav">
  <a class="active">Home</a><a>Tiles</a><a>Systems</a><a>Gallery</a><a>About</a><a>Contact us</a>
</nav>

<div class="abs hero" role="img" aria-label="Photo of a bright living room with warm wood floor, tan sofas and glass table"></div>
<div class="abs caption">
  <h2>Clean Design Tiles</h2>
  <p>You can describe your slides using captions. This is an example of a caption with <a>a link</a>.</p>
</div>
<div class="abs dots"><span></span><span class="on"></span><span></span><span></span><span></span></div>
<div class="abs hero-arrows">
  <span><svg width="8" height="10"><path d="M6 1 2 5 6 9" fill="none" stroke="#fff" stroke-width="1.5"/></svg></span>
  <span><svg width="8" height="10"><path d="M2 1 6 5 2 9" fill="none" stroke="#fff" stroke-width="1.5"/></svg></span>
</div>

<div class="abs callout">
  <h3>We offer counter tops. tile for floors, showers, kitchen backsplashes and more..</h3>
  <p>Lorem ipsum dolor sit amet, consectetuer adipiscing elit, sed diam nonummy nibh euismod tincidunt ut laoreet dolore magna aliquam erat volutpat sed diam nonummy.</p>
  <div class="btn">Learn More</div>
</div>

<div class="abs section-title" style="left:183px;top:576px">Selected Projects <em>– <i>View All Projects »</i></em></div>
<div class="abs mini-arrows" style="left:987px;top:578px">
  <span><svg width="6" height="8"><path d="M5 1 2 4 5 7" fill="none" stroke="#fff" stroke-width="1.3"/></svg></span>
  <span><svg width="6" height="8"><path d="M1 1 4 4 1 7" fill="none" stroke="#fff" stroke-width="1.3"/></svg></span>
</div>
<div class="abs section-rule" style="left:183px;top:607px;width:839px"></div>

<div class="abs project" style="left:183px"><div class="thumb" role="img" aria-label="Photo of a white dining room with wood floor"></div><h4>White Dining Room</h4></div>
<div class="abs project" style="left:397px"><div class="thumb" role="img" aria-label="Photo of a living room with large windows"></div><h4>Living with Large Windows</h4></div>
<div class="abs project" style="left:612px"><div class="thumb dark" role="img" aria-label="Photo of a brown living room with dark wall"></div><h4>Brown Living Room</h4>
  <span class="nudge" style="left:0"><svg width="8" height="10"><path d="M6 1 2 5 6 9" fill="none" stroke="#fff" stroke-width="1.5"/></svg></span>
  <span class="nudge" style="right:0"><svg width="8" height="10"><path d="M2 1 6 5 2 9" fill="none" stroke="#fff" stroke-width="1.5"/></svg></span>
</div>
<div class="abs project" style="left:825px"><div class="thumb" role="img" aria-label="Photo of a sunny living room with garden view"></div><h4>Self-Hosted Project</h4></div>

<div class="abs section-title" style="left:183px;top:812px">Newsletter Subscription</div>
<div class="abs section-rule" style="left:183px;top:845px;width:410px"></div>
<p class="abs news-copy">Subscribe to our email newsletter for useful tips and valuable resources sent out every second Monday.</p>
<div class="abs field">Enter your email address here ...</div>
<div class="abs btn subscribe">Subscribe</div>
<p class="abs note"><b>*</b> Check your spam folder if the mail does not arrive.</p>

<div class="abs section-title" style="left:610px;top:812px">Testimonials <em>– <i>View All Testimonials »</i></em></div>
<div class="abs mini-arrows" style="left:985px;top:814px">
  <span><svg width="6" height="8"><path d="M5 1 2 4 5 7" fill="none" stroke="#fff" stroke-width="1.3"/></svg></span>
  <span><svg width="6" height="8"><path d="M1 1 4 4 1 7" fill="none" stroke="#fff" stroke-width="1.3"/></svg></span>
</div>
<div class="abs section-rule" style="left:610px;top:845px;width:410px"></div>
<blockquote class="abs quote"><span class="mark">“</span>Lorem ipsum dolor sit amet, consectetuer adipiscing elit, sed diam nonummy nibh euismod tincidunt ut laoreet dolore magna aliquam erat volutpat nibh euismod ut laoreet.</blockquote>
<svg class="abs quote-tail" width="16" height="9"><path d="M0 0 8 8 16 0" fill="#fafafa" stroke="#e3e3e3"/></svg>
<div class="abs author" style="top:964px;color:var(--ink)">Mara Ellison, Coastal Region</div>
<div class="abs author" style="top:980px;color:var(--muted)">Brightfold Studio</div>

<footer class="abs footer">
  <span class="copy">Copyright © 2014 Quarry-Mosaic Artisans. All rights reserved.</span>
  <span class="links">Home<i>·</i>Tiles<i>·</i>Systems<i>·</i>Gallery<i>·</i>About us<i>·</i>Contact</span>
</footer>
<div class="abs to-top"><svg width="12" height="8"><path d="M1 7 6 2 11 7" fill="none" stroke="#fff" stroke-width="1.6"/></svg></div>
</body>
</html>
```